Verpackungsaufkleber kreieren für Kaninchenheu
Zielgruppe
Wir ernten und vertreiben hochwertiges Futter (insbesondere Heu/Stroh) für Kaninchen und alle Heimtiere. Wir vertreiben derzeit unsere Produkte vorranging über unseren Online-Shop (www.strohkörbchen.de). Da wir uns der ökologischen und naturverbundenen Verpackung verbunden haben, möchten wir die Papier-Verpackung entsprechend hochwertig und ansprechend in die Regale der Einzelhändler zum Verkauf anbieten. Unsere Zielgruppe im Onlineshop sind meist Frauen, 16-50 J., welche besonderen Wert auf Qualität und ansprechende Verpackung legen.
Aufgabenstellung
Wir haben uns zu dem Design überlegt, dass es toll wäre, wenn der Kunde unsere Heu-Produkte in einer Papierverpackung in den Regalen sieht und ein Label in Form eines 'durchsichtigen Fensters' auf der Verpackung klebt, welches imitiert, dass es einen tatsächlichen Einblick in die Papiertüte auf das hochwertige Heu gewährt.
Also dass der Kunde den Eindruck hat, dass Heu in Form eines Fensters zu sehen. Dabei soll jedoch auch unser aktuelles Logo am Rand miteingebunden werden, sowie einen Textbereich mit ein paar Informationen zum Heu. Sofern Kapazitäten und interessante Neugestaltung des Logos eingebracht werden können würden wir auch hierbei überlegen unser aktuelles Logo auszuwechseln.
Die weitere Überlegung wäre, einen Aufkleber für beide Verpackungsvarianten (Papiertüten und Plastiktüten) zu kreieren . Hierzu gibt es keine Überlegungen unserseits. Dies würde den Vorteil mit sich bringen, dass wir nur eine Vorlage als Aufkleber drucken müssen. D.h. der oben beschriebenen Vorschlag dient hauptsächlich dazu, dass der Kunde eine Vorstellung hat, welches Produkt sich darin befindet, wobei man bei der durchsichtigen Plastiktüte das Produkt natürlich sehen kann und hierbei das Heu als Bild nicht zwingend in diesem Sichtfenster vollflächig dargestellt werden müsste.
Als Idee könnte man auch noch die regionale Eifellandschaft mit einbinden.
Diese Ausgestaltung möchten wir aber Euch und Euren kreativen Köpfen überlassen.
Wir freuen uns über interessante Vorschläge!

```html
<!DOCTYPE html>
<html lang="de">
<head>
<meta charset="utf-8">
<title>Strohkörbchen – Etiketten Qualitätsheu</title>
<link rel="stylesheet" href="https://fonts.googleapis.com/css2?family=Montserrat:wght@400;600;700&display=swap">
<style>
  :root {
    --stage: #dedede;
    --label: #ffffff;
    --label-soft: #f8f8fa;
    --ink: #231f20;
    --ink-body: #3a3a3a;
    --hay-light: #c9c7cc;
    --hay-mid: #9aa08f;
    --hay-dark: #5c6356;
    --brand-dot: #b48a55;
  }
  * { box-sizing: border-box; margin: 0; padding: 0; }
  html, body {
    width: 1200px; height: 800px; overflow: hidden;
    background: var(--stage);
    font-family: "Montserrat", sans-serif;
    color: var(--ink);
  }
  .label-set {
    position: absolute; left: 50px; top: 130px;
    display: flex; gap: 40px; align-items: flex-start;
  }
  .label {
    position: relative;
    width: 340px; height: 540px;
    background: var(--label);
    border-radius: 22px;
    padding: 28px 36px 30px;
    display: flex; flex-direction: column; align-items: center;
  }
  .label--soft { background: var(--label-soft); }
  .hay-window {
    width: 210px; height: 250px;
    border-radius: 105px 105px 14px 14px;
    background:
      linear-gradient(115deg, transparent 40%, rgba(255,255,255,.25) 48%, transparent 56%),
      radial-gradient(circle at 35% 30%, var(--hay-light), transparent 60%),
      linear-gradient(160deg, var(--hay-mid), var(--hay-dark) 55%, var(--hay-mid));
  }
  .brand {
    margin-top: 18px;
    display: flex; align-items: center; gap: 10px;
    font-weight: 700; font-size: 32px; letter-spacing: -0.5px;
    color: var(--ink);
  }
  .brand-dot {
    width: 22px; height: 22px; border-radius: 50%;
    background: var(--brand-dot);
  }
  .corner-mark {
    position: absolute; top: 22px; right: 22px;
    display: flex; flex-direction: column; align-items: center; gap: 5px;
    font-weight: 600; font-size: 8px; letter-spacing: .6px; color: var(--ink);
  }
  .corner-mark .brand-dot { width: 30px; height: 30px; }
  .product-title {
    margin-top: auto;
    font-weight: 700; font-size: 17px; text-align: center;
  }
  .product-text {
    margin-top: 12px;
    font-size: 12.5px; line-height: 1.45; text-align: justify;
    color: var(--ink-body);
  }
</style>
</head>
<body>
  <main class="label-set">
    <article class="label">
      <div class="corner-mark"><span class="brand-dot"></span>STROHKÖRBCHEN.DE</div>
      <div class="hay-window" role="img" aria-label="Sichtfenster mit Foto von hochwertigem Heu"></div>
      <div class="brand">Strohkörbchen</div>
      <h2 class="product-title">Qualitätsheu aus Eifel</h2>
      <p class="product-text">Lorem ipsum dolor sit amet, consectetur adipisici elit, sed eiusmod tempor incidunt ut labore et dolore magna aliqua.</p>
    </article>

    <article class="label label--soft">
      <div class="hay-window" role="img" aria-label="Sichtfenster mit Foto von hochwertigem Heu"></div>
      <div class="brand"><span class="brand-dot"></span>Strohkörbchen</div>
      <h2 class="product-title">Qualitätsheu aus Eifel</h2>
      <p class="product-text">Lorem ipsum dolor sit amet, consectetur adipisici elit, sed eiusmod tempor incidunt ut labore et dolore magna aliqua.</p>
    </article>

    <article class="label">
      <div class="hay-window" role="img" aria-label="Sichtfenster mit Foto von hochwertigem Heu"></div>
      <div class="brand"><span class="brand-dot"></span>Strohkörbchen</div>
      <h2 class="product-title">Qualitätsheu aus Eifel</h2>
      <p class="product-text">Lorem ipsum dolor sit amet, consectetur adipisici elit, sed eiusmod tempor incidunt ut labore et dolore magna aliqua.</p>
    </article>
  </main>
</body>
</html>
```